Crumbly Corner needs a business card

Crumbly Corner needs an attractive, playful, and exciting business card design to attract potential buyers. I have included our logo, label, and social media design files along with the fonts and colors for ideas. For the logo file, please only pay attention to the purple background with white text. I want a card with premium matte and metallic finish. I want my name included, e-mail, and phone number. The logo must be included, and then use the label design and social media design files to add creativity to the design. Only the fonts that are provided should be used as well.

Name: Gregory Halvorsen
Phone: 555-274-8106
E-mail: ghalvorsen@crumblycornerco.example

Industry/Entity Type

Business

Contact Information for Business Card

I want a card with premium matte and metallic finish. I want my name included, e-mail, and phone number. The logo must be included, and then use the label design and social media design files to add creativity to the design. Only the fonts that are provided should be used as well.

Name: Gregory Halvorsen
Phone: 555-274-8106

Colors
6b449b

Requirements
Must have
• My logo, my fonts, my colors, my designs to some degree, and my character

```html
<!DOCTYPE html>
<html lang="en">
<head>
<meta charset="utf-8">
<title>Crumbly Corner – Business Card</title>
<link rel="stylesheet" href="https://fonts.googleapis.com/css2?family=Caudex&family=Arimo&display=swap">
<style>
  :root {
    --page-bg: #a6a8aa;
    --card-deep: #2a0d4f;
    --card-mid: #3e1b6e;
    --card-glow: #6b3596;
    --gold: #d9b066;
    --skyline: #2c1150;
  }
  * { margin: 0; padding: 0; box-sizing: border-box; }
  html, body { width: 953px; height: 1200px; overflow: hidden; }
  body { background: var(--page-bg); position: relative; font-family: "Arimo", Arial, sans-serif; }

  .card {
    position: absolute;
    overflow: hidden;
    background: radial-gradient(ellipse at 50% 45%, var(--card-glow) 0%, var(--card-mid) 45%, var(--card-deep) 100%);
    box-shadow: 0 14px 24px rgba(0,0,0,0.28);
  }
  .card-front { left: 45px; top: 85px; width: 858px; height: 487px; }
  .card-back  { left: 48px; top: 613px; width: 855px; height: 489px;
    background: radial-gradient(ellipse at 57% 48%, var(--card-glow) 0%, var(--card-mid) 42%, var(--card-deep) 100%); }

  .star-pattern {
    position: absolute; inset: 0;
    background: linear-gradient(180deg, rgba(30,8,60,0.35) 0%, rgba(30,8,60,0) 40%);
  }
  .skyline {
    position: absolute; left: 0; right: 0; bottom: 0; height: 140px;
    background: linear-gradient(180deg, rgba(44,17,80,0) 0%, rgba(44,17,80,0.7) 55%, #220a45 100%);
  }

  .brand-name {
    position: absolute;
    font-family: "Caudex", Georgia, serif;
    color: var(--gold);
    text-align: center;
    line-height: 1.05;
  }
  .card-front .brand-name { left: 0; right: 0; top: 190px; font-size: 52px; }
  .card-back .brand-name { left: 60px; width: 200px; top: 200px; font-size: 40px; }

  .divider {
    position: absolute; left: 330px; top: 94px; width: 2px; height: 286px;
    background: var(--gold);
  }

  .person-name {
    position: absolute; left: 445px; top: 160px;
    font-family: "Caudex", Georgia, serif;
    font-size: 32px; color: var(--gold);
  }
  .contact-list { position: absolute; left: 438px; top: 275px; list-style: none; }
  .contact-item {
    display: flex; align-items: center; gap: 14px;
    color: var(--gold); font-size: 20px; height: 40px;
  }
  .contact-item svg { width: 26px; height: 22px; flex: none; }
</style>
</head>
<body>
  <section class="card card-front">
    <div class="star-pattern" role="img" aria-label="Faint star pattern beneath an arched frame"></div>
    <div class="skyline" role="img" aria-label="Silhouette of a domed city skyline"></div>
    <div class="brand-name">Crumbly Corner</div>
  </section>

  <section class="card card-back">
    <div class="star-pattern" role="img" aria-label="Faint star pattern"></div>
    <div class="skyline" role="img" aria-label="Silhouette of a domed city skyline"></div>
    <div class="brand-name">Crumbly Corner</div>
    <div class="divider"></div>
    <div class="person-name">Gregory Halvorsen</div>
    <ul class="contact-list">
      <li class="contact-item">
        <svg viewBox="0 0 24 24" aria-hidden="true"><path fill="#d9b066" d="M6.6 10.8a15 15 0 0 0 6.6 6.6l2.2-2.2a1 1 0 0 1 1-.25 11.4 11.4 0 0 0 3.6.57 1 1 0 0 1 1 1V20a1 1 0 0 1-1 1A17 17 0 0 1 3 4a1 1 0 0 1 1-1h3.5a1 1 0 0 1 1 1c0 1.25.2 2.45.57 3.57a1 1 0 0 1-.25 1z"/></svg>
        <span>555-274-8106</span>
      </li>
      <li class="contact-item">
        <svg viewBox="0 0 26 20" aria-hidden="true"><rect x="1" y="1" width="24" height="18" fill="none" stroke="#d9b066" stroke-width="1.8"/><path d="M1 1l12 10L25 1M1 19l9-8M25 19l-9-8" fill="none" stroke="#d9b066" stroke-width="1.6"/></svg>
        <span>ghalvorsen@crumblycornerco.example</span>
      </li>
    </ul>
  </section>
</body>
</html>
```